Redesign of Bright Harbor Entertainment Card

I already have my logo and font design for my company name. I am looking to come up with a Unique way of having it on my business card. Just looking for a really hip, and professional business card while still using my logo design.

I have also enclosed the front and back of the card so you can see what I have now. Looking for something different.

Thank you!

Target Market(s)

Young to middle aged brides and grooms

Industry/Entity Type

Business

Requirements
Should not have
• Cheese

```html
<!DOCTYPE html>
<html lang="en">
<head>
<meta charset="utf-8">
<title>Bright Harbor Entertainment – Business Card</title>
<link href="https://fonts.googleapis.com/css2?family=Arimo:wght@400;700&display=swap" rel="stylesheet">
<style>
  :root {
    --page: #ffffff;
    --card: #000000;
    --card-top: #3a3a3a;
    --brand: #2f7fd6;
    --brand-light: #29a9e8;
    --text: #ffffff;
    --wave-gold: #b8a84a;
    --wave-blue: #5a63b8;
  }
  * { margin: 0; padding: 0; box-sizing: border-box; }
  html, body {
    width: 900px; height: 1200px; overflow: hidden;
    background: var(--page);
    font-family: "Arimo", Arial, sans-serif;
    color: var(--text);
  }
  .card {
    position: absolute; left: 8px; width: 884px; height: 441px;
    background: linear-gradient(to bottom, var(--card-top) 0%, var(--card) 32%, var(--card) 100%);
    overflow: hidden;
  }
  .card--front { top: 55px; }
  .card--back { top: 510px; }

  .brand { position: absolute; display: flex; align-items: center; }
  .brand__mark { border: 3px solid var(--brand-light); border-radius: 50%; flex: none; }
  .brand__text { display: flex; flex-direction: column; }
  .brand__name {
    color: var(--brand); font-weight: 700; letter-spacing: 3px; line-height: 1; text-transform: uppercase;
  }
  .brand__tagline {
    color: var(--brand); font-weight: 400; text-transform: uppercase; letter-spacing: 0.3px;
  }
  .card--front .brand { left: 185px; top: 12px; gap: 14px; }
  .card--front .brand__mark { width: 146px; height: 126px; }
  .card--front .brand__name { font-size: 58px; }
  .card--front .brand__tagline { font-size: 12.5px; margin-top: 8px; }
  .card--back .brand { left: 17px; top: 15px; gap: 10px; }
  .card--back .brand__mark { width: 96px; height: 84px; }
  .card--back .brand__name { font-size: 38px; letter-spacing: 2px; }
  .card--back .brand__tagline { font-size: 8.5px; margin-top: 5px; }

  .waveform {
    position: absolute; left: 0; width: 100%; height: 150px;
    background:
      linear-gradient(to bottom, rgba(0,0,0,0) 0%, rgba(0,0,0,0) 12%, rgba(0,0,0,0.2) 22%, rgba(0,0,0,1) 100%),
      linear-gradient(to right, var(--wave-blue) 0%, rgba(150,150,170,0.6) 25%, var(--wave-gold) 50%, rgba(150,150,170,0.6) 75%, var(--wave-blue) 100%);
    opacity: 0.55;
  }
  .card--front .waveform { top: 140px; }
  .card--back .waveform { top: 100px; }

  .contact { position: absolute; left: 60px; top: 283px; }
  .contact__name { font-size: 38px; line-height: 1.1; margin-bottom: 10px; }
  .contact__line { font-size: 15px; line-height: 20px; letter-spacing: 0.3px; }
  .contact__line--small { font-size: 14px; }

  .links { position: absolute; right: 21px; bottom: 8px; text-align: right; font-size: 15px; line-height: 19px; letter-spacing: 0.3px; }

  .services__intro { position: absolute; left: 24px; top: 243px; font-size: 21px; letter-spacing: 0.3px; }
  .services__list { position: absolute; left: 338px; top: 270px; list-style: none; }
  .services__item { font-size: 29px; line-height: 34px; letter-spacing: 0.4px; position: relative; padding-left: 40px; }
  .services__item::before {
    content: ""; position: absolute; left: 3px; top: 15px; width: 8px; height: 8px; border-radius: 50%; background: var(--text);
  }
</style>
</head>
<body>
  <section class="card card--front">
    <div class="brand">
      <span class="brand__mark"></span>
      <div class="brand__text">
        <span class="brand__name">Bright Harbor</span>
        <span class="brand__tagline">Entertainment &amp; Event Professionals</span>
      </div>
    </div>
    <div class="waveform" role="img" aria-label="Audio waveform band"></div>
    <div class="contact">
      <p class="contact__name">Dan Porter</p>
      <p class="contact__line">Owner/ DJ/ Emcee</p>
      <p class="contact__line contact__line--small">555-014-DJDJ(3535)</p>
      <p class="contact__line">info@brightharborsounds.com</p>
    </div>
    <div class="links">
      <p>brightharborsounds.com</p>
      <p>facebook.com/brightharborentertainment</p>
    </div>
  </section>

  <section class="card card--back">
    <div class="brand">
      <span class="brand__mark"></span>
      <div class="brand__text">
        <span class="brand__name">Bright Harbor</span>
        <span class="brand__tagline">Entertainment &amp; Event Professionals</span>
      </div>
    </div>
    <div class="waveform" role="img" aria-label="Audio waveform band"></div>
    <p class="services__intro">We provide services such as:</p>
    <ul class="services__list">
      <li class="services__item">DJ/ Emcees</li>
      <li class="services__item">Lighting/ Wireless LED Uplight</li>
      <li class="services__item">Photo Booth</li>
      <li class="services__item">Photo Montages</li>
    </ul>
  </section>
</body>
</html>
```